Tidewell Outdoor Signage

We need an outdoor signage design for my company with new logo designed from makerhive. We do electrical, Air conditioning & Plumbing, installation, service, repairs and maintenance. The design shall be an eye catching that cannot miss ready it.

Industry/Entity Type

Electrical, Air conditioning, Plumbing

```html
<!DOCTYPE html>
<html lang="en">
<head>
<meta charset="utf-8">
<title>Tidewell Outdoor Signage</title>
<link rel="stylesheet" href="https://fonts.googleapis.com/css2?family=Prompt:wght@400;500&display=swap">
<style>
  :root {
    --stage: #6a6a6a;
    --sign-red: #e8202a;
    --sign-blue: #1b6aab;
    --white: #ffffff;
    --brand-orange: #ef7f22;
    --photo-dark: #4c4f55;
    --photo-mid: #b9bcc2;
    --photo-light: #f1f2f4;
  }
  * { margin: 0; padding: 0; box-sizing: border-box; }
  html, body {
    width: 1200px; height: 1000px; overflow: hidden;
    background: var(--stage);
    font-family: "Prompt", sans-serif;
  }
  .sign {
    position: absolute; left: 158px; top: 255px;
    width: 892px; height: 463px; overflow: hidden;
    background: var(--photo-light);
  }
  .sign__photo {
    position: absolute; left: 0; top: 0; width: 892px; height: 255px;
    background: linear-gradient(90deg, var(--photo-dark) 0%, #7d8088 30%, var(--photo-mid) 55%, var(--photo-light) 70%, #e6e7ea 100%);
  }
  .service-tab {
    position: absolute; left: 0; top: 157px; width: 592px; height: 98px;
  }
  .service-tab__text {
    position: absolute; left: 52px; top: 167px;
    color: var(--white); font-size: 29px; font-weight: 400; line-height: 40px;
    letter-spacing: 0.2px;
  }
  .brand {
    position: absolute; left: 645px; top: 60px; width: 200px;
    text-align: center;
  }
  .brand__mark {
    width: 64px; height: 64px; border-radius: 50%;
    background: var(--sign-blue); margin: 0 auto 14px;
  }
  .brand__name {
    color: var(--brand-orange); font-size: 42px; font-weight: 500; line-height: 42px;
  }
  .brand__tagline {
    color: var(--sign-blue); font-size: 11px; font-weight: 500; margin-top: 4px;
    white-space: nowrap;
  }
  .contact-band {
    position: absolute; left: 0; top: 255px; width: 892px; height: 208px;
    background: var(--sign-red); color: var(--white); text-align: center;
  }
  .contact-band__phone {
    font-size: 112px; font-weight: 500; line-height: 112px;
    margin-top: 34px; letter-spacing: 1px;
  }
  .contact-band__links {
    font-size: 19px; font-weight: 500; margin-top: 12px; letter-spacing: 0.3px;
  }
</style>
</head>
<body>
  <div class="sign">
    <div class="sign__photo" role="img" aria-label="Photo of a gloved technician testing a switchboard with a multimeter, blending into an outdoor air conditioning unit being serviced"></div>
    <svg class="service-tab" viewBox="0 0 592 98" aria-hidden="true">
      <path d="M0 0 H536 Q550 0 558 12 L592 98 H0 Z" fill="var(--sign-blue)"/>
    </svg>
    <p class="service-tab__text">Air Conditioning Repairs,<br>Installation &amp; Service Adelaide</p>
    <div class="brand">
      <div class="brand__mark"></div>
      <div class="brand__name">Tidewell</div>
      <div class="brand__tagline">Electrical &nbsp;Air Conditioning &nbsp;Plumbing</div>
    </div>
    <div class="contact-band">
      <div class="contact-band__phone">0400 555 172</div>
      <div class="contact-band__links">INFO@TIDEWELLELECTRICAL.COM.AU &nbsp;|&nbsp; WWW.TIDEWELLELECTRICAL.COM.AU</div>
    </div>
  </div>
</body>
</html>
```